Layout für Longboardshop
Zielgruppe
Online Shop für Longboards, basierend auf Kassalo 4.1.2
Zielgruppe: Sportliche Menschen mit Hang zum Wellenreiten, Surfen,Kiten, Snowboarden oder Skateboarden.
Aufgabenstellung
Erstellung des Grunddesigns (Header, Footer, Menü, Detailansicht, Buttons) als PSD. Die Umsetzung in ein Template erledigen wir alleine.
Neugründung: Es existieren noch keine Logos oder Farbvorgaben.
We have no site, it is a completly new project. There are no limits concerning colors, fonts etc.
Competitors:
http://www.brettgleiter-zone.de
http://fenwick-rollbretter.de/
http://www.rollbrettladen.de/
http://www.kerbo.de/de_DE/Skateboard/Longboards.html?sid=1
http://www.pumeri-boards.de/
I think, big pictures transporting the surfstyle attitude of this sport works good.
Der Grundaufbau sollte sich an http://www.kassalodemo.de/ anlehnen, um den Anpassungsaufwand mgl. überschaubar zu halten.

```html
<!DOCTYPE html>
<html lang="de">
<head>
<meta charset="utf-8">
<title>Rollwerk-Markt – Longboardshop</title>
<link rel="stylesheet" href="https://fonts.googleapis.com/css2?family=Source+Sans+3:wght@400;600;700&display=swap">
<style>
:root{
  --teal:#1a82a6;
  --teal-dark:#12698a;
  --teal-text:#1f8fb5;
  --dark:#3a3a3a;
  --darker:#2f2f2f;
  --grey-btn:#4a4a4a;
  --page:#e9e9e9;
  --white:#ffffff;
  --text:#333333;
  --muted:#666666;
  --line:#dcdcdc;
}
*{box-sizing:border-box;margin:0;padding:0}
html,body{width:1200px;height:1200px;overflow:hidden}
body{position:relative;background:var(--page);font-family:"Source Sans 3",Arial,sans-serif;color:var(--text);font-size:9px}
.abs{position:absolute}

.topbar{left:0;top:0;width:1200px;height:22px;background:var(--dark);display:flex;justify-content:flex-end;padding-right:240px}
.topbar__item{display:flex;align-items:center;gap:6px;padding:0 10px;color:#ddd;font-size:7px;border-left:1px solid #4e4e4e}
.topbar__item:last-child{border-right:1px solid #4e4e4e}
.flag{width:12px;height:8px;background:linear-gradient(#000 0 33%,#d00 33% 66%,#fc0 66%)}

.logo{left:240px;top:31px;width:216px;height:75px;background:var(--white);display:flex;align-items:center;justify-content:center}
.logo__name{color:var(--teal);font-weight:700;font-size:24px}

.search{left:790px;top:34px;width:170px;height:17px;background:var(--white);border:1px solid #ccc;border-radius:3px;font-size:6.5px;color:#888;padding:4px 8px;display:flex;justify-content:space-between}
.cart{left:790px;top:60px;width:170px;height:55px;background:var(--white)}
.cart__top{display:flex;align-items:center;height:40px;padding-left:10px;border-bottom:1px solid var(--line)}
.cart__bag{width:20px;height:24px;background:#b8d3e0;border-radius:2px}
.cart__label{font-size:8px;margin-left:14px;width:70px}
.cart__total{border-left:1px solid var(--line);height:26px;padding-left:12px;font-size:7px;text-align:center;line-height:10px}
.cart__info{font-size:7.5px;text-align:center;padding-top:3px}
.cart__info b{color:var(--teal-text);font-weight:400}

.nav{left:240px;top:120px;width:720px;height:29px;display:flex;align-items:flex-end}
.nav__home{width:68px;height:29px;background:var(--white);display:flex;align-items:center;justify-content:center}
.nav__home span{border:1px solid var(--teal);color:var(--teal);font-weight:600;font-size:8px;padding:3px 12px}
.nav__item{height:23px;background:linear-gradient(var(--teal),var(--teal-dark));color:#fff;font-weight:600;font-size:8px;display:flex;align-items:center;justify-content:center;border-left:1px solid #0f5d78}

.hero{left:240px;top:149px;width:720px;height:240px;background:var(--white)}
.hero__shadow{left:250px;top:388px;width:700px;height:6px;background:radial-gradient(ellipse at top,rgba(0,0,0,.35),transparent 70%)}
.strip{top:169px;width:57px;height:200px}
.strip__arrow{position:absolute;right:-1px;top:70px;width:12px;height:58px;background:var(--white);color:#e7962a;font-size:10px;display:flex;align-items:center;justify-content:center}
.banner{left:462px;top:169px;width:473px;height:200px;background:linear-gradient(135deg,#0e5f8c,#3aa6d6 55%,#0c5a88)}
.banner__text{position:absolute;right:16px;bottom:7px;color:#fff;font-weight:700;text-align:right;line-height:1}
.banner__text .big{font-size:35px}
.banner__text .small{font-size:19px}

.sidebar{left:240px;top:414px;width:173px;height:570px;background:var(--white);padding:9px 9px}
.side__head{height:23px;background:linear-gradient(var(--teal),var(--teal-dark));color:#fff;font-weight:600;font-size:8px;display:flex;align-items:center;justify-content:center}
.side__box{background:#fbfbfb;border:1px solid #eee;margin:3px 0}
.check{display:flex;align-items:center;height:24px;padding-left:23px;font-size:8px;color:#555}
.check i{width:10px;height:10px;border:1px solid #ddd;border-radius:2px;background:#f4f4f4;margin-right:15px;display:flex;align-items:center;justify-content:center}
.check.on{font-size:9.5px;color:#222;font-weight:600}
.range{height:70px;position:relative;font-size:8px}
.filter{display:flex;gap:4px;margin-top:5px}
.filter__reset{width:40px;height:21px;background:var(--grey-btn);display:flex;align-items:center;justify-content:center}
.filter__go{flex:1;height:21px;background:linear-gradient(var(--teal),var(--teal-dark));color:#fff;font-size:8px;font-weight:600;display:flex;align-items:center;justify-content:center}

.tab{background:var(--white);padding:6px 11px;height:28px}
.tab span{display:inline-block;border:1px solid var(--teal);color:var(--teal);font-size:8px;font-weight:600;padding:3px 13px}
.panel{background:var(--white);display:flex;padding:13px 0 0 10px}
.product{width:162px;text-align:center}
.product__img{height:150px;margin:0 auto 12px;border-radius:40px}
.product__title{font-size:11px;font-weight:600;color:#111}
.product__desc{font-size:7.5px;line-height:11px}
.product__btns{display:flex;justify-content:center;gap:3px;margin-top:5px}
.btn{height:21px;color:#fff;font-size:7.5px;font-weight:600;display:flex;align-items:center;padding:0 6px}
.btn--details{background:var(--grey-btn)}
.btn--cart{background:linear-gradient(var(--teal),var(--teal-dark))}
.pager{width:24px;display:flex;flex-direction:column}
.pager div{flex:1;display:flex;align-items:center;justify-content:center}
.pager .prev{background:#bdbdbd}
.pager .next{background:linear-gradient(var(--teal),var(--teal-dark))}

.footer{left:0;top:1036px;width:1200px;height:140px;background:var(--dark);border-top:2px solid var(--teal);color:#eee;font-size:8px}
.footer h3{font-size:8.5px;font-weight:400;color:#fff}
.footer h3 em{font-style:normal;color:var(--teal-text)}
.footer a{color:var(--teal-text);text-decoration:none}
.fcol{position:absolute;top:33px}
.fgrid{display:grid;gap:0 13px;margin-top:17px;line-height:15.6px}
.copyright{left:0;top:1176px;width:1200px;height:24px;background:var(--teal-dark);color:#eee;font-size:7.5px;display:flex;align-items:center;justify-content:center}
</style>
</head>
<body>

<div class="abs topbar">
  <div class="topbar__item"><svg width="9" height="9" viewBox="0 0 10 10"><circle cx="5" cy="3" r="2.5" fill="#ddd"/><path d="M0 10q5-6 10 0z" fill="#ddd"/></svg>Mein Konto</div>
  <div class="topbar__item"><svg width="8" height="10" viewBox="0 0 8 10"><rect x="0.5" y="1" width="7" height="8.5" fill="none" stroke="#ddd"/><path d="M2 5l1.5 1.5L6 3.5" stroke="#ddd" fill="none"/></svg>Merkzettel</div>
  <div class="topbar__item"><svg width="10" height="10" viewBox="0 0 10 10"><path d="M1 1l8 8M9 1L1 9" stroke="#ddd" stroke-width="1.6"/></svg>Service/Hilfe</div>
  <div class="topbar__item"><svg width="7" height="5" viewBox="0 0 7 5"><path d="M0.5 0.5l3 3 3-3" stroke="#ddd" fill="none" stroke-width="1.4"/></svg>EUR</div>
  <div class="topbar__item"><svg width="7" height="5" viewBox="0 0 7 5"><path d="M0.5 0.5l3 3 3-3" stroke="#ddd" fill="none" stroke-width="1.4"/></svg><span class="flag"></span></div>
</div>

<div class="abs logo"><span class="logo__name">rollwerk-markt.de</span></div>

<div class="abs search"><span>Suchbegriff eingeben</span><svg width="7" height="7" viewBox="0 0 8 8"><circle cx="5" cy="3" r="2.3" stroke="#555" fill="none"/><path d="M3.4 4.6L0.8 7.2" stroke="#555" stroke-width="1.3"/></svg></div>
<div class="abs cart">
  <div class="cart__top"><div class="cart__bag"></div><div class="cart__label">WARENKORB</div><div class="cart__total">Total:<br><b>84,95€</b></div></div>
  <div class="cart__info">Es befinden sich <b>2 Artikel</b> im Warenkorb.</div>
</div>

<nav class="abs nav">
  <div class="nav__home"><span>HOME</span></div>
  <div class="nav__item" style="width:107px">DECKS</div>
  <div class="nav__item" style="width:112px">ZUBEHÖR</div>
  <div class="nav__item" style="width:105px">% SALE</div>
  <div class="nav__item" style="width:91px">TEAM</div>
  <div class="nav__item" style="width:108px">BILDER</div>
  <div class="nav__item" style="width:129px">KONTAKT</div>
</nav>

<div class="abs hero"></div>
<div class="abs hero__shadow"></div>
<div class="abs strip" style="left:263px;background:linear-gradient(#d9a24a,#e6a13a 40%,#8a3a6a)" role="img" aria-label="Foto: Longboarder im Sonnenuntergang"><div class="strip__arrow">»</div></div>
<div class="abs strip" style="left:329px;background:linear-gradient(#5b9aa0,#c9a57a 50%,#2a2a2a)" role="img" aria-label="Foto: Longboard an einer Wand"><div class="strip__arrow">»</div></div>
<div class="abs strip" style="left:395px;background:linear-gradient(#444,#bbb 50%,#777)" role="img" aria-label="Foto: Fahrerin auf dem Longboard, schwarzweiß"><div class="strip__arrow" style="color:#bbb">»</div></div>
<div class="abs banner" role="img" aria-label="Foto: Surfbrett in der Welle">
  <div class="banner__text"><div class="big">ON %SALE!</div><div class="small">VON 05.09. BIS 30.09.</div></div>
</div>

<aside class="abs sidebar">
  <div class="side__head">MARKE</div>
  <div class="side__box" style="height:235px;padding-top:12px">
    <div class="check"><i></i>Auswahl #1</div>
    <div class="check on"><i><svg width="7" height="6" viewBox="0 0 7 6"><path d="M0.8 3l2 2L6.2 0.8" stroke="#1a6f95" stroke-width="1.4" fill="none"/></svg></i>Auswahl #2</div>
    <div class="check"><i></i>Auswahl #3</div>
    <div class="check"><i></i>Auswahl #4</div>
    <div class="check"><i></i>Auswahl #5</div>
    <div class="check"><i></i>Auswahl #6</div>
    <div class="check"><i></i>Auswahl #7</div>
    <div class="check"><i></i>Auswahl #8</div>
    <div class="check"><i></i>Auswahl #9</div>
  </div>
  <div class="side__head" style="margin-top:3px">PREISKLASSE</div>
  <div class="side__box range">
    <span class="abs" style="left:39px;top:15px">100€</span>
    <span class="abs" style="left:97px;top:14px">200€</span>
    <svg class="abs" style="left:16px;top:28px" width="122" height="10" viewBox="0 0 122 10"><path d="M2 5h118" stroke="#444" stroke-width="2"/><path d="M2 1v8M32 3v5M61 3v5M90 3v5M120 1v8" stroke="#444"/><circle cx="61" cy="5" r="3" fill="#fff" stroke="#444"/></svg>
    <span class="abs" style="left:8px;top:43px">&lt;50€</span>
    <span class="abs" style="left:68px;top:41px;font-size:10px;font-weight:700">150€</span>
    <span class="abs" style="left:125px;top:43px">250€&lt;</span>
  </div>
  <div class="side__head" style="margin-top:3px">ZUBEHÖR</div>
  <div class="side__box" style="height:125px;padding-top:15px">
    <div class="check"><i></i>Auswahl #1</div>
    <div class="check on"><i><svg width="7" height="6" viewBox="0 0 7 6"><path d="M0.8 3l2 2L6.2 0.8" stroke="#1a6f95" stroke-width="1.4" fill="none"/></svg></i>Auswahl #2</div>
    <div class="check"><i></i>Auswahl #3</div>
    <div class="check"><i></i>Auswahl #4</div>
  </div>
  <div class="filter">
    <div class="filter__reset"><svg width="13" height="13" viewBox="0 0 14 14"><path d="M11.5 7A4.5 4.5 0 1 1 7 2.5" stroke="#fff" stroke-width="1.6" fill="none"/><path d="M6 0l3 2.5L6 5z" fill="#fff"/></svg></div>
    <div class="filter__go">FILTER STARTEN</div>
  </div>
</aside>

<section class="abs" style="left:444px;top:413px;width:516px">
  <div class="tab" style="width:98px"><span>TOPSELLER</span></div>
  <div style="display:flex;height:252px">
    <div class="panel" style="flex:1">
      <div class="product"><div class="product__img" style="width:85px;background:linear-gradient(90deg,#3a3e44 50%,#2f8fa6 50%,#d95a4a)" role="img" aria-label="Produktfoto: Longboard mit bunter Grafik"></div><div class="product__title">ARTIKELBEZEICHNUNG</div><div class="product__desc">Lorem Ipsum. Proin gravidanv.<br>Preis: <b>123,00€</b> inkl. MwSt.</div><div class="product__btns"><span class="btn btn--details">DETAILS</span><span class="btn btn--cart">IN DEN WARENKORB</span></div></div>
      <div class="product"><div class="product__img" style="width:80px;background:linear-gradient(90deg,#b8925e 50%,#a98a6c 50%,#6a8a8a)" role="img" aria-label="Produktfoto: Bambus-Longboard"></div><div class="product__title">ARTIKELBEZEICHNUNG</div><div class="product__desc">Lorem Ipsum. Proin gravidanv.<br>Preis: <b>123,00€</b> inkl. MwSt.</div><div class="product__btns"><span class="btn btn--details">DETAILS</span><span class="btn btn--cart">IN DEN WARENKORB</span></div></div>
      <div class="product"><div class="product__img" style="width:88px;background:linear-gradient(90deg,#2c2c2e 50%,#6a5a3a 50%,#c8922c)" role="img" aria-label="Produktfoto: Downhill-Longboard mit gelben Rollen"></div><div class="product__title">ARTIKELBEZEICHNUNG</div><div class="product__desc">Lorem Ipsum. Proin gravidanv.<br>Preis: <b>123,00€</b> inkl. MwSt.</div><div class="product__btns"><span class="btn btn--details">DETAILS</span><span class="btn btn--cart">IN DEN WARENKORB</span></div></div>
    </div>
    <div class="pager"><div class="prev"><svg width="6" height="9" viewBox="0 0 6 9"><path d="M5 1L1.5 4.5 5 8" stroke="#fff" stroke-width="1.6" fill="none"/></svg></div><div class="next"><svg width="6" height="9" viewBox="0 0 6 9"><path d="M1 1l3.5 3.5L1 8" stroke="#fff" stroke-width="1.6" fill="none"/></svg></div></div>
  </div>

  <div class="tab" style="width:128px;margin-top:11px"><span>ZULETZT VERKAUFT</span></div>
  <div style="display:flex;height:253px">
    <div class="panel" style="flex:1">
      <div class="product"><div class="product__img" style="width:125px;height:80px;margin:35px auto 47px;background:linear-gradient(#d8d8d8,#8a8a8a)" role="img" aria-label="Produktfoto: Longboard-Achse"></div><div class="product__title">ARTIKELBEZEICHNUNG</div><div class="product__desc">Lorem Ipsum. Proin gravidanv.<br>Preis: <b>123,00€</b> inkl. MwSt.</div><div class="product__btns"><span class="btn btn--details">DETAILS</span><span class="btn btn--cart">IN DEN WARENKORB</span></div></div>
      <div class="product"><div class="product__img" style="width:80px;background:linear-gradient(90deg,#b8925e 50%,#a98a6c 50%,#6a8a8a)" role="img" aria-label="Produktfoto: Bambus-Longboard"></div><div class="product__title">ARTIKELBEZEICHNUNG</div><div class="product__desc">Lorem Ipsum. Proin gravidanv.<br>Preis: <b>123,00€</b> inkl. MwSt.</div><div class="product__btns"><span class="btn btn--details">DETAILS</span><span class="btn btn--cart">IN DEN WARENKORB</span></div></div>
      <div class="product"><div class="product__img" style="width:100px;height:100px;margin:30px auto 32px;border-radius:50%;background:radial-gradient(#fff 20%,#555 45%,#eee 75%)" role="img" aria-label="Produktfoto: Longboard-Rolle"></div><div class="product__title">ARTIKELBEZEICHNUNG</div><div class="product__desc">Lorem Ipsum. Proin gravidanv.<br>Preis: <b>123,00€</b> inkl. MwSt.</div><div class="product__btns"><span class="btn btn--details">DETAILS</span><span class="btn btn--cart">IN DEN WARENKORB</span></div></div>
    </div>
    <div class="pager"><div class="prev"><svg width="6" height="9" viewBox="0 0 6 9"><path d="M5 1L1.5 4.5 5 8" stroke="#fff" stroke-width="1.6" fill="none"/></svg></div><div class="next"><svg width="6" height="9" viewBox="0 0 6 9"><path d="M1 1l3.5 3.5L1 8" stroke="#fff" stroke-width="1.6" fill="none"/></svg></div></div>
  </div>
</section>

<footer class="abs footer">
  <div class="fcol" style="left:240px">
    <h3><em>ROLLWERK-MARKT.DE</em> SITEMAP</h3>
    <div class="fgrid" style="grid-template-columns:30px 30px auto">
      <span>Home</span><span>Team</span><span>Mein Konto</span>
      <span>Decks</span><span>Bilder</span><span>Datenschutz</span>
      <span>Zubehör</span><span>Kontakt</span><span>Merkzettel</span>
      <span>Sale</span><span>AGB</span><span>Impressum</span>
    </div>
  </div>
  <div class="fcol" style="left:454px">
    <h3><em>ROLLWERK-MARKT.DE</em> KONTAKT</h3>
    <div class="fgrid" style="grid-template-columns:95px auto">
      <b>rollwerk-markt.de</b><span>T: 12345 - 67 89 01 12 34</span>
      <span>Rollwerkstraße 1</span><span>F: 12345 - 67 89 02 12 35</span>
      <span>12345 Rollwerkstadt</span><span>M: <a>info@rollwerk-markt.de</a></span>
      <span>Deutschland</span><span>W: <a>www.rollwerk-markt.de</a></span>
    </div>
  </div>
  <div class="fcol" style="left:750px;width:212px">
    <h3><em>ROLLWERK-MARKT.DE</em> VERSANDINFOS</h3>
    <p style="margin-top:17px;line-height:15.6px">Lorem Ipsum. Proin gravida nibh vel velit auctor aliquet. Aenean sollicitudin, lorem quis bibendum auctor, nisi elit consequat ipsum, nec sagittis sem nibh id elit. Duis sed odio sit amet nibh vulputate cursus a sit amet mauris.</p>
  </div>
</footer>
<div class="abs copyright">Copyright © 2013 Rollwerkname &nbsp;|&nbsp; Alle Rechte vorbehalten.</div>

</body>
</html>
```